The Wisdom of Lanterns New Book Cover Design Project

Book cover design . Paperback, ebook, and Talvora (derived from book cover) files/images required.
Book Title: The Wisdom of Lanterns
Subtitle: Under Copper Bridges
Author: Daniel Forsythe
Files: Ebook, Paperback (Brindlewick & Halvern Quill), Talvora sized image
File size & information to be provided once design is ready. Brindlewick paperback will be 5.25 x 8.
Completion date is flexible. Planning to publish in November.
Updates

Target Market(s)

Motorcycle owners

Font styles to use
Sans Serif

Requirements
Must have
• A generic looking motorcycle (samples attached). Thumbnail easily recognized as a motorcycle book.
Nice to have
• Open to all ideas but am favoring my idea: to emphasize the title lettering similar to (but not a copy of) other Wisdom books (examples attached), on a plain background. All books in the category have a motorcycle on the cover. Author name and subtitle do not have to be prominent. Rider optional..
Should not have
• Should not look like a biker romance or fantasy cover or look cartoonish. Motorcycle pic should be fairly generic (brand, style,).

```html
<!DOCTYPE html>
<html lang="en">
<head>
<meta charset="utf-8">
<title>The Wisdom of Lanterns — New Book Cover Design</title>
<link rel="stylesheet" href="https://fonts.googleapis.com/css2?family=Montserrat:wght@400;700&family=Raleway:wght@400;500&display=swap">
<style>
  :root {
    --page-bg: #ffffff;
    --navy: #12135e;
    --cover-text: #ffffff;
    --cover-text-soft: rgba(255, 255, 255, 0.92);
  }
  * { margin: 0; padding: 0; box-sizing: border-box; }
  html, body {
    width: 1200px;
    height: 1200px;
    overflow: hidden;
    background: var(--page-bg);
  }
  .presentation {
    position: relative;
    width: 1200px;
    height: 1200px;
    font-family: "Montserrat", sans-serif;
  }
  .presentation-title {
    position: absolute;
    top: 29px;
    left: 0;
    width: 100%;
    text-align: center;
    color: var(--navy);
    font-weight: 700;
    font-size: 20px;
    line-height: 26px;
    letter-spacing: 0.5px;
    text-transform: uppercase;
  }
  .design {
    position: absolute;
    width: 315px;
  }
  .design--01 { left: 242px; top: 116px; }
  .design--02 { left: 643px; top: 116px; }
  .design--03 { left: 242px; top: 645px; }
  .design--04 { left: 643px; top: 645px; }

  .cover {
    position: relative;
    width: 315px;
    height: 473px;
    overflow: hidden;
    color: var(--cover-text);
  }

  /* Sky with leaping rider, top of the cover */
  .cover-sky {
    position: absolute;
    left: 0;
    top: 0;
    width: 100%;
    height: 62%;
  }
  /* Motorcycle close-up, lower cover */
  .cover-motorcycle {
    position: absolute;
    left: 0;
    top: 40%;
    width: 100%;
    height: 60%;
    -webkit-mask-image: linear-gradient(180deg, transparent 0%, #000 14%);
    mask-image: linear-gradient(180deg, transparent 0%, #000 14%);
  }

  .design--01 .cover-sky {
    background:
      radial-gradient(ellipse at 55% 40%, #fbf6ef 0%, rgba(246,236,226,0.85) 35%, rgba(0,0,0,0) 70%),
      linear-gradient(180deg, #b9bdb0 0%, #e7dcd2 45%, #d8c9cf 100%);
  }
  .design--01 .cover-motorcycle {
    background:
      radial-gradient(ellipse at 40% 45%, #4a3d58 0%, rgba(74,61,88,0.6) 35%, rgba(0,0,0,0) 65%),
      linear-gradient(180deg, #c9b8c6 0%, #7d6a84 30%, #5c4d68 55%, #9a94a0 78%, #6f7a5c 100%);
  }
  .design--02 .cover-sky {
    background:
      radial-gradient(ellipse at 45% 45%, #f3dcae 0%, rgba(236,214,170,0.6) 28%, rgba(0,0,0,0) 60%),
      linear-gradient(180deg, #5f9fba 0%, #9cc3d0 50%, #a8b8d8 100%);
  }
  .design--02 .cover-motorcycle {
    background:
      radial-gradient(ellipse at 40% 45%, #3e4670 0%, rgba(62,70,112,0.6) 35%, rgba(0,0,0,0) 65%),
      linear-gradient(180deg, #a3abd0 0%, #6a73a2 30%, #4f5784 55%, #a9b1c6 78%, #7f8f72 100%);
  }
  .design--03 .cover-sky {
    background:
      radial-gradient(ellipse at 45% 45%, #f2b43a 0%, rgba(236,170,60,0.75) 22%, rgba(0,0,0,0) 55%),
      linear-gradient(180deg, #4a5e5a 0%, #7fb7b2 50%, #5b7c82 100%);
  }
  .design--03 .cover-motorcycle {
    background:
      radial-gradient(ellipse at 40% 45%, #232838 0%, rgba(35,40,56,0.7) 35%, rgba(0,0,0,0) 65%),
      linear-gradient(180deg, #6c7c86 0%, #3a4052 30%, #2b3042 55%, #e6dcb8 78%, #9fa04c 100%);
  }
  .design--04 .cover-sky {
    background:
      radial-gradient(ellipse at 45% 45%, #e4b561 0%, rgba(220,176,100,0.55) 22%, rgba(0,0,0,0) 55%),
      linear-gradient(180deg, #7b6e74 0%, #8fb1b5 50%, #7d8aa0 100%);
  }
  .design--04 .cover-motorcycle {
    background:
      radial-gradient(ellipse at 40% 45%, #3d3e5a 0%, rgba(61,62,90,0.6) 35%, rgba(0,0,0,0) 65%),
      linear-gradient(180deg, #9a9cb4 0%, #5d5f7e 30%, #4b4c69 55%, #b3b8c6 78%, #86957a 100%);
  }

  .cover-author,
  .cover-subtitle {
    position: absolute;
    left: 0;
    width: 100%;
    text-align: center;
    font-family: "Montserrat", sans-serif;
    font-weight: 400;
    font-size: 10.5px;
    letter-spacing: 3.2px;
    text-transform: uppercase;
    color: var(--cover-text-soft);
  }
  .cover-author { top: 23px; }
  .cover-subtitle { top: 446px; }

  .cover-title {
    position: absolute;
    top: 140px;
    left: 0;
    width: 100%;
    text-align: center;
    font-family: "Raleway", sans-serif;
    font-weight: 500;
    text-transform: uppercase;
    color: var(--cover-text);
  }
  .cover-title-main {
    display: block;
    font-size: 35px;
    line-height: 44px;
    letter-spacing: 1px;
  }
  .cover-title-sub {
    display: block;
    margin-top: 2px;
    font-size: 18px;
    line-height: 22px;
    letter-spacing: 5px;
  }

  .design-label {
    margin-top: 11px;
    text-align: center;
    color: var(--navy);
    font-weight: 700;
    font-size: 17px;
    letter-spacing: 0.4px;
    text-transform: uppercase;
  }
</style>
</head>
<body>
<main class="presentation">
  <h1 class="presentation-title">The Wisdom of Lanterns<br>New Book Cover Design</h1>

  <section class="design design--01">
    <div class="cover">
      <div class="cover-sky" role="img" aria-label="Hazy pale sunlit sky with a faint rider silhouette leaping"></div>
      <div class="cover-motorcycle" role="img" aria-label="Close-up photo of a generic chrome motorcycle with shock absorbers, footpeg and exhaust, in soft violet light"></div>
      <p class="cover-author">Daniel Forsythe</p>
      <h2 class="cover-title"><span class="cover-title-main">The Wisdom</span><span class="cover-title-sub">of Lanterns</span></h2>
      <p class="cover-subtitle">Under Copper Bridges</p>
    </div>
    <p class="design-label">Design 01</p>
  </section>

  <section class="design design--02">
    <div class="cover">
      <div class="cover-sky" role="img" aria-label="Blue cloudy sky with a rider silhouette leaping"></div>
      <div class="cover-motorcycle" role="img" aria-label="Close-up photo of a generic chrome motorcycle with shock absorbers, footpeg and exhaust, in cool blue tones"></div>
      <p class="cover-author">Daniel Forsythe</p>
      <h2 class="cover-title"><span class="cover-title-main">The Wisdom</span><span class="cover-title-sub">of Lanterns</span></h2>
      <p class="cover-subtitle">Under Copper Bridges</p>
    </div>
    <p class="design-label">Design 02</p>
  </section>

  <section class="design design--03">
    <div class="cover">
      <div class="cover-sky" role="img" aria-label="Teal and gold sunset sky with a rider silhouette leaping"></div>
      <div class="cover-motorcycle" role="img" aria-label="Close-up photo of a generic chrome motorcycle with shock absorbers, footpeg and exhaust, on sunlit gravel"></div>
      <p class="cover-author">Daniel Forsythe</p>
      <h2 class="cover-title"><span class="cover-title-main">The Wisdom</span><span class="cover-title-sub">of Lanterns</span></h2>
      <p class="cover-subtitle">Under Copper Bridges</p>
    </div>
    <p class="design-label">Design 03</p>
  </section>

  <section class="design design--04">
    <div class="cover">
      <div class="cover-sky" role="img" aria-label="Muted sunset sky with a rider silhouette leaping"></div>
      <div class="cover-motorcycle" role="img" aria-label="Close-up photo of a generic chrome motorcycle with shock absorbers, footpeg and exhaust, in muted violet tones"></div>
      <p class="cover-author">Daniel Forsythe</p>
      <h2 class="cover-title"><span class="cover-title-main">The Wisdom</span><span class="cover-title-sub">of Lanterns</span></h2>
      <p class="cover-subtitle">Under Copper Bridges</p>
    </div>
    <p class="design-label">Design 04</p>
  </section>
</main>
</body>
</html>
```